Book Cover for my Autobiography

I would like to see a CONCEPT of the Front Cover as per the following.
a) Take me out of the FILE NAMED=1-MAIN.jpg
b) I want my Wife "Watching over me" - behind me - in the SHADOWS. You can take her image for the concept from the FILE NAMED=2-Wife Watching over me.jpg.
c) This based on the old saying that "Behind every Good Man....is a Woman".  So that's what I want to convert because my wife has always been in the background, in the "Shadows" - always supporting and encouraging me in whatever I do.
d) This book is purely for my children, wife, siblings, relatives and Friends.
e) the Book Cover has to be designed FLAT & RECTANGULAR - like the sample leather cover.  i.e. NOT viewed from an Angle.
f) The Book Title is "Salt in the Orchard"
g) I have no pre-conceived ideas of design or colours or styling etc.  I want a PROFESSIONAL DESIGNER to come up with the best Overall Design that conveys the "Supportive Wife" always behind me and supporting me - While I am out front as the subject.
h) When the Design is accepted, I will provide the main photo of my wife without my son in front of her that I want to use - and one me without my wife's arms around me.  But if you can do that too (i.e. reconstruct my Wife's Burgundy top & and remove her arms from around me-then even better because I don't have to hire another graphic designer to do that for me).
My name is "Tomas Brenhoek" so the author of the autobiography needs to be SOMEWHERE.
h) And last, please just put some text - maybe 2 sentences for the summary of the story like many Autobiographies do. eg.
"My story of how ....Lorem ipsum dolor sit amet, consectetur adipiscing elit, sed do eiusmod tempor incididunt. Integer vitae justo eget magna fermentum iaculis eu non. Aliquam eleifend".

I forgot to mention that this Book Cover is actually going on an eBOOK - not a Printed Book.
It's just for Family and Friends.

```html
<!DOCTYPE html>
<html lang="en">
<head>
<meta charset="utf-8">
<title>Salt in the Orchard – Book Cover</title>
<link rel="stylesheet" href="https://fonts.googleapis.com/css2?family=Great+Vibes&family=Open+Sans:wght@400&display=swap">
<style>
  :root {
    --page-bg: #fdd98a;
    --cover-top: #962249;
    --cover-bottom: #861b3c;
    --band-light: #a8406a;
    --band-deep: #6e1733;
    --portrait-wife-a: #7d2547;
    --portrait-wife-b: #8f2248;
    --portrait-author-hair: #1b1c2e;
    --portrait-author-skin: #8a5a4c;
    --portrait-author-shirt: #243c8c;
    --text-light: #ffffff;
  }
  * { margin: 0; padding: 0; box-sizing: border-box; }
  html, body {
    width: 1200px; height: 1200px; overflow: hidden;
    background: var(--page-bg);
  }
  .book-cover {
    position: absolute;
    left: 207px; top: 40px;
    width: 785px; height: 1120px;
    overflow: hidden;
    background: linear-gradient(180deg, var(--cover-top) 0%, var(--cover-bottom) 100%);
  }
  .cover-art {
    position: absolute; inset: 0;
    width: 100%; height: 100%;
  }
  .title {
    position: absolute; left: 0; top: 0;
    width: 100%; height: 320px;
    font-family: "Great Vibes", cursive;
    color: var(--text-light);
    font-weight: 400;
    text-shadow: 2px 3px 4px rgba(40, 0, 15, 0.55);
    line-height: 1;
  }
  .title span { position: absolute; white-space: nowrap; }
  .title .line-1 { left: 468px; top: 62px; font-size: 92px; }
  .title .line-2 { left: 372px; top: 140px; font-size: 88px; }
  .title .line-3 { left: 452px; top: 205px; font-size: 92px; }
  .blurb {
    position: absolute; left: 67px; top: 748px;
    width: 300px;
    font-family: "Open Sans", sans-serif;
    font-size: 15.5px;
    line-height: 31.6px;
    color: var(--text-light);
  }
  .author {
    position: absolute; left: 64px; top: 972px;
    font-family: "Open Sans", sans-serif;
    font-size: 40px;
    font-weight: 400;
    color: var(--text-light);
    white-space: nowrap;
  }
</style>
</head>
<body>
  <main class="book-cover">
    <svg class="cover-art" viewBox="0 0 872 1244" preserveAspectRatio="none" aria-hidden="false">
      <defs>
        <radialGradient id="wifeGlow" cx="50%" cy="45%" r="55%">
          <stop offset="0%" stop-color="var(--portrait-wife-a)"/>
          <stop offset="70%" stop-color="var(--portrait-wife-b)" stop-opacity="0.8"/>
          <stop offset="100%" stop-color="var(--cover-top)" stop-opacity="0"/>
        </radialGradient>
        <linearGradient id="authorTone" x1="0" y1="0" x2="0" y2="1">
          <stop offset="0%" stop-color="var(--portrait-author-hair)"/>
          <stop offset="35%" stop-color="var(--portrait-author-skin)"/>
          <stop offset="62%" stop-color="var(--portrait-author-skin)"/>
          <stop offset="75%" stop-color="var(--portrait-author-shirt)"/>
          <stop offset="100%" stop-color="var(--portrait-author-shirt)"/>
        </linearGradient>
      </defs>

      <!-- upper sweeping band -->
      <path class="band band-upper" fill="var(--band-light)" opacity="0.55"
        d="M0,490 C120,520 220,610 360,615 C470,618 530,520 560,380 C600,250 700,150 872,120
           L872,260 C760,270 700,330 660,430 C610,560 520,690 360,690 C220,690 120,640 0,630 Z"/>

      <!-- lower dark field -->
      <path class="band band-deep" fill="var(--band-deep)" opacity="0.45"
        d="M0,640 C120,650 220,700 360,695 C520,690 610,560 660,440 L872,430 L872,1244 L0,1244 Z"/>

      <!-- lower light band -->
      <path class="band band-lower" fill="var(--band-light)" opacity="0.6"
        d="M0,1225 C90,1130 170,1000 330,960 C520,915 700,880 872,825
           L872,905 C700,960 520,985 380,1030 C240,1080 160,1180 110,1244 L0,1244 Z"/>

      <!-- wife portrait area -->
      <ellipse role="img" aria-label="Soft shadowed portrait of the author's wife, watching over him"
        cx="255" cy="360" rx="230" ry="300" fill="url(#wifeGlow)"/>

      <!-- author portrait area -->
      <path role="img" aria-label="Portrait photograph of the author, Tomas Brenhoek, smiling"
        fill="url(#authorTone)"
        d="M650,490 C760,490 830,560 830,680 C830,800 800,880 760,920
           C830,960 872,990 872,1010 L872,1244 L285,1244
           C320,1120 420,1000 520,950 C490,880 480,790 480,690 C480,560 550,490 650,490 Z"/>
    </svg>

    <h1 class="title" aria-label="Salt in the Orchard">
      <span class="line-1">Salt in</span>
      <span class="line-2">the</span>
      <span class="line-3">Orchard</span>
    </h1>

    <p class="blurb">"My story of how ....Lorem ipsum dolor<br>sit amet,<br>onsectetur adipiscing elit,<br>sed do eiusmod tempor incididunt.<br>Integer vitae justo eget<br>magna fermentum iaculis eu non.<br>Aliquam eleifend".</p>

    <p class="author">Tomas Brenhoek</p>
  </main>
</body>
</html>
```